Business Card Design Project

Double sided business card - logo on one side, my details on the other.

I would like to see two options - my logo on a dark grey/black background and my logo on white.

My details as follows:

Trevin Howsam MBus, MRQT
P: 0471 520 164
E: trevin@trevinhowsam.com
W: www.trevinhowsam.com

Target Market(s)

Managers in business, universities and government.

Industry/Entity Type

Business

Requirements
Must have
• Quorvel, Mintaglo and Brastonet icons

```html
<!DOCTYPE html>
<html lang="en">
<head>
<meta charset="utf-8">
<title>Trevin Howsam – Business Cards</title>
<link rel="stylesheet" href="https://fonts.googleapis.com/css2?family=Anton&family=Arimo&family=Pathway+Gothic+One&display=swap">
<style>
  :root {
    --ink: #000000;
    --paper: #ffffff;
    --card-tint: #fbfdfe;
    --accent-blue: #6b9bff;
    --detail-blue: #3d6595;
    --detail-ink: #222222;
    --mark-grey: #c9c9c9;
    --mark-dark: #3a3a3a;
    --rule-blue: #5b8ee6;
    --edge: #333333;
  }
  html, body {
    margin: 0;
    padding: 0;
    width: 1002px;
    height: 1200px;
    overflow: hidden;
    background: var(--paper);
  }
  .sheet {
    position: relative;
    width: 1002px;
    height: 1200px;
  }
  .card {
    position: absolute;
    left: 0;
    width: 1000px;
    border: 1px solid var(--edge);
    background: var(--card-tint);
    overflow: hidden;
  }
  .card--front { top: 0; height: 569px; }
  .card--back  { top: 624px; height: 574px; }

  .backdrop-shape {
    position: absolute;
    box-sizing: border-box;
  }
  .card--front .backdrop-shape {
    left: 60px; top: -40px; width: 880px; height: 620px;
    border: 34px solid var(--mark-grey);
    opacity: 0.55;
  }

  .wordmark {
    position: absolute;
    left: 124px;
    top: 192px;
    margin: 0;
    font-family: "Anton", "Impact", sans-serif;
    font-weight: 400;
    font-size: 106px;
    line-height: 1;
    letter-spacing: 4px;
    color: var(--ink);
    text-transform: uppercase;
    white-space: nowrap;
  }
  .wordmark__surname { color: var(--accent-blue); }
  .tagline {
    position: absolute;
    left: 126px;
    top: 316px;
    margin: 0;
    font-family: "Arimo", "Arial", sans-serif;
    font-size: 42px;
    line-height: 1;
    color: var(--ink);
    white-space: nowrap;
  }

  .details-panel {
    position: absolute;
    left: 0; top: 0;
    width: 507px; height: 100%;
    background: var(--card-tint);
    overflow: hidden;
  }
  .panel-rule {
    position: absolute;
    left: 507px; top: 0;
    width: 7px; height: 100%;
    background: var(--rule-blue);
  }
  .mark-panel {
    position: absolute;
    left: 514px; top: 0;
    right: 0; height: 100%;
    background: var(--ink);
    overflow: hidden;
  }
  .mark-panel .backdrop-shape {
    left: 10px; top: 60px; width: 560px; height: 480px;
    border: 30px solid var(--mark-dark);
  }

  .contact {
    position: absolute;
    left: 70px;
    margin: 0;
    font-family: "Pathway Gothic One", "Oswald", sans-serif;
    font-size: 45px;
    line-height: 1;
    color: var(--detail-ink);
    white-space: nowrap;
  }
  .contact__label { color: var(--detail-blue); }
  .contact--name  { top: 71px;  color: var(--detail-blue); }
  .contact--phone { top: 173px; }
  .contact--email { top: 270px; }
  .contact--web   { top: 365px; }

  .social-list {
    position: absolute;
    left: 84px;
    top: 458px;
    margin: 0;
    padding: 0;
    list-style: none;
    display: flex;
    gap: 20px;
  }
  .social-list__item {
    display: flex;
    align-items: center;
    gap: 8px;
    font-family: "Pathway Gothic One", "Oswald", sans-serif;
    font-size: 28px;
    line-height: 1;
    color: var(--detail-blue);
  }
  .social-list__square {
    width: 26px;
    height: 26px;
    background: var(--detail-blue);
  }
</style>
</head>
<body>
<main class="sheet">

  <section class="card card--front" aria-label="Business card front">
    <div class="backdrop-shape" aria-hidden="true"></div>
    <h1 class="wordmark">Trevin<span class="wordmark__surname">Howsam</span></h1>
    <p class="tagline">Business advice, research and training.</p>
  </section>

  <section class="card card--back" aria-label="Business card back">
    <div class="details-panel">
      <p class="contact contact--name">Trevin Howsam MBus, MRQT</p>
      <p class="contact contact--phone"><span class="contact__label">P:</span> 0471 520 164</p>
      <p class="contact contact--email"><span class="contact__label">E:</span> trevin@trevinhowsam.com</p>
      <p class="contact contact--web"><span class="contact__label">W:</span> www.trevinhowsam.com</p>
      <ul class="social-list">
        <li class="social-list__item"><span class="social-list__square"></span>Mintaglo</li>
        <li class="social-list__item"><span class="social-list__square"></span>Quorvel</li>
        <li class="social-list__item"><span class="social-list__square"></span>Brastonet</li>
      </ul>
    </div>
    <div class="panel-rule"></div>
    <div class="mark-panel">
      <div class="backdrop-shape" aria-hidden="true"></div>
    </div>
  </section>

</main>
</body>
</html>
```